Packaging design for high end, natural skin care line needed

Marisol Thackery Beauty needs a label design. It is a new skin care line I am launching.
For years my line Velvet Orchard Beauty was quite popular and featured in several magazines, but for personal reasons had to be shut down. Now I am launching a new line featuring VOB's top selling products, but focused solely on skin care more so than cosmetics. All products will still be handmade, but the line should still look professional-something worthy of a Brindle Market shelf!
I am branding it with my name, as I am often quoted in articles related to gluten in beauty products, so Marisol Thackery and beauty are key words.
The key products will be facial and body serums which are packaged in .5oz., 1oz. and larger amber glass bottles with black dropper tops, I will include pictures below. For dimensions, the labels can be any size that you think will work best, but need to at the least fit the 1oz. bottle, dimensions shown here http://www.corvelflask.example/amber-glass-tall-round-flask/p/QZ7K-93/
I loved the former VOB logo, but for Marisol Thackery Beauty I am looking for something more personal, more apothecary-like, and probably less colorful.
The line will be small, just a handful of products, but luxe, rich.
I am attaching photos of Velvet Orchard Beauty's packaging for your reference.
Thanks much!!

Hi Everyone! Thank you for your submissions! Please see the links I provided in the brief, I really am looking for something more technical looking, like an apothecary. And want black text on a white background, not a black background, and nothing flowery.
Thank you all!!
Marisol

Target Market(s)

My clients are primarily women of all ages, but with more of a skin care focus, and no longer a cosmetic one, I would also like to appeal to a male audience. My clients are health conscious, gluten-free, natural, paleo, or vegan, etc. Target age is probably 25-55. Products are a bit high end, priced $45-65.

Industry/Entity Type

Cosmetics

Requirements
Must have
• It must at least say Marisol Thackery, or can say Marisol Thackery Beauty, but "Beauty" is not necessary. And capitalization is open, try whatever you think serves the brand. Likely slogans or taglines that can be included but are not essential: Care for your skin. Love and care for your skin. Handmade with love in the USA. Handmade in the USA. Think modern day apothecary. Small batch scotch. Something fine, but custom, handmade.
Nice to have
• I like the aesthetic of Oribel Skin Care a bit http://www.oribelhollis.example.au/
And of Dorian Valtz as shown here http://www.pinboardia.example/pin/847302915563017442/
Also of something like this that is even customizable http://www.pinboardia.example/pin/58274106392285514/
Every product is handmade in small batches, with fine ingredients, a moderate price point of around $45-$65. And I will likely begin making custom orders. So there could be a space to say when it was made, or for whom. I would like to keep the colors classic though, I probably want to stay away from the bright pink on this one.
Should not have
• As I mentioned, probably want to stay away from a lot of color. I like black vs. gray for the text, as it will show up better in editorials. I must look good, but also photograph well. Thanks!

```html
<!DOCTYPE html>
<html lang="en">
<head>
<meta charset="utf-8">
<title>Marisol Thackery – Balancing Facial Serum Label</title>
<link href="https://fonts.googleapis.com/css2?family=Didact+Gothic&family=Fira+Sans:wght@400&display=swap" rel="stylesheet">
<style>
  :root {
    --ink: #111111;
    --paper: #ffffff;
    --accent: #1fb25e;
  }
  html, body {
    margin: 0;
    padding: 0;
    width: 1200px;
    height: 574px;
    overflow: hidden;
    background: var(--paper);
  }
  .label {
    position: relative;
    width: 1200px;
    height: 574px;
    background: var(--paper);
    color: var(--ink);
    font-family: "Fira Sans", sans-serif;
    overflow: hidden;
  }
  .band {
    position: absolute;
    left: 0;
    width: 1200px;
    height: 10px;
    background: var(--accent);
  }
  .band--top { top: 0; }
  .band--bottom { bottom: 0; }

  .rule {
    position: absolute;
    height: 1px;
    background: var(--ink);
  }

  .brand-name {
    position: absolute;
    top: 46px;
    left: 0;
    width: 1200px;
    margin: 0;
    text-align: center;
    font-family: "Didact Gothic", sans-serif;
    font-weight: 400;
    font-size: 60px;
    line-height: 64px;
    letter-spacing: 0.5px;
  }
  .tagline {
    position: absolute;
    top: 116px;
    left: 0;
    width: 1200px;
    margin: 0;
    text-align: center;
    font-family: "Didact Gothic", sans-serif;
    font-size: 22px;
    letter-spacing: 0.5px;
  }

  .details {
    position: absolute;
    left: 23px;
    top: 108px;
    width: 340px;
    font-size: 13.5px;
    line-height: 18.5px;
  }
  .details p { margin: 0 0 18.5px; }

  .ingredients {
    position: absolute;
    right: 24px;
    top: 154px;
    width: 380px;
    text-align: right;
    font-size: 13.5px;
    line-height: 18.5px;
  }
  .ingredients p { margin: 0 0 18.5px; }

  .mark {
    position: absolute;
    top: 236px;
    left: 0;
    width: 1200px;
    display: flex;
    justify-content: center;
    align-items: center;
    gap: 14px;
  }
  .mark-dot {
    width: 30px;
    height: 30px;
    border-radius: 50%;
    background: var(--ink);
  }
  .mark-name {
    font-family: "Didact Gothic", sans-serif;
    font-size: 30px;
    line-height: 36px;
  }

  .product-name {
    position: absolute;
    top: 356px;
    left: 0;
    width: 1200px;
    margin: 0;
    text-align: center;
    font-family: "Didact Gothic", sans-serif;
    font-weight: 400;
    font-size: 28px;
    line-height: 34px;
  }
  .product-strike {
    position: absolute;
    top: 379px;
    left: 425px;
    width: 348px;
    height: 3px;
    background: var(--accent);
  }

  .origin {
    position: absolute;
    top: 434px;
    left: 0;
    width: 1200px;
    margin: 0;
    text-align: center;
    font-family: "Didact Gothic", sans-serif;
    font-size: 22px;
    letter-spacing: 0.5px;
  }
</style>
</head>
<body>
<div class="label">
  <div class="band band--top"></div>

  <div class="rule" style="left:22px; top:61px; width:333px;"></div>
  <div class="rule" style="left:22px; top:99px; width:328px;"></div>
  <div class="rule" style="left:848px; top:61px; width:328px;"></div>
  <div class="rule" style="left:851px; top:99px; width:325px;"></div>

  <h1 class="brand-name">Marisol Thackery</h1>
  <p class="tagline">- care for your skin -</p>

  <div class="details">
    <p>BALANCING FACIAL SERUM 0.5 OZ</p>
    <p>Balane, calm and nurture. Astringent<br>
       Hazelnut and Evening Primrose Oils<br>
       benefit acne/oil prone skin.<br>
       Anti-Oxidant rich Pomegranate Oil<br>
       calms redness.</p>
    <p>DIRECTIONS: After washing apply pea-sized<br>
       amount to palm, massage palms together,<br>
       gently press onto face.<br>
       Use in the morning and evening.</p>
    <p>100% Vegan, Gluten-Free,<br>
       Cruelty-Fre, No Animal Testing</p>
    <p>100%&nbsp; Natural.<br>
       Please discard after six months.</p>
  </div>

  <div class="ingredients">
    <p>INGREDIENTS:<br>
       pomegranate seed oil*,<br>
       evening primrose oil*, hazelnut oil,<br>
       borage oil, kukui nut oil, sea buckthorn oil,<br>
       vitamin E oil (from Non-GMO soy)*,<br>
       essential oils of frankincense*,<br>
       helichrysum and palmarosa*.<br>
       Contains soy and nut oils.</p>
    <p>*Certified Organic</p>
    <p>www.velvetorchardbeauty.example</p>
  </div>

  <div class="mark">
    <span class="mark-dot"></span>
    <span class="mark-name">Marisol Thackery</span>
  </div>

  <h2 class="product-name">Balancing Facial Serum</h2>
  <div class="product-strike"></div>

  <div class="rule" style="left:22px; top:447px; width:426px;"></div>
  <p class="origin">handmade in the USA</p>
  <div class="rule" style="left:746px; top:447px; width:430px;"></div>

  <div class="band band--bottom"></div>
</div>
</body>
</html>
```